Stationary Design Letterhead and Envelope

Artist should provide Letterhead and envelop stationary designs

Info for stationary:
Fernhallow Outdoor Advertising
4873 Quarry Rd. 915 N. PO BOX 528617
Austin, TX 78519

Dale Fernhallow
President
555-862-1907
dale@fernhallowsigns.example
fernhallowsigns.example

Target Market(s)

clients

Colors
0054AA
0677BA
7BADD7
CADEEF
E8F1F8

Requirements
Must have
• high quality unique eye catching and dynamic

```html
<!DOCTYPE html>
<html lang="en">
<head>
<meta charset="utf-8">
<title>Fernhallow Outdoor Advertising – Stationery</title>
<link rel="stylesheet" href="https://fonts.googleapis.com/css2?family=Arimo:wght@400;700&family=Montserrat:wght@600&display=swap">
<style>
  :root {
    --brand-blue: #0677BA;
    --brand-deep: #0054AA;
    --ink: #000000;
    --text-gray: #555555;
    --paper: #ffffff;
    --paper-shade: #eeeef1;
    --backdrop: #c4c4c4;
  }
  * { box-sizing: border-box; margin: 0; padding: 0; }
  html, body { width: 1200px; height: 1164px; overflow: hidden; }
  body {
    position: relative;
    background: var(--backdrop);
    font-family: "Arimo", Arial, sans-serif;
    color: var(--text-gray);
  }
  .sheet {
    position: absolute;
    background: linear-gradient(135deg, var(--paper) 0%, var(--paper) 45%, var(--paper-shade) 100%);
    box-shadow: 2px 3px 6px rgba(0,0,0,.25);
    overflow: hidden;
  }
  .brand-band { position: absolute; left: 0; right: 0; display: flex; }
  .brand-band .band-blue { background: var(--brand-blue); }
  .brand-band .band-black { background: var(--ink); flex: 1; }
  .brand-rule { position: absolute; left: 0; right: 0; height: 1.5px; background: var(--ink); }
  .brand-name {
    position: absolute; left: 0; right: 0; text-align: center;
    font-family: "Montserrat", Arial, sans-serif; font-weight: 600;
    text-transform: uppercase; white-space: nowrap; color: #fff; letter-spacing: .02em;
  }

  /* Business card front */
  .card-front { left: 154px; top: 58px; width: 425px; height: 242px; }
  .card-front .brand-band { top: 43px; height: 31px; }
  .card-front .band-blue { width: 207px; }
  .card-front .brand-name { top: 50px; font-size: 15px; }
  .card-front .brand-rule { top: 85px; }
  .card-person { position: absolute; right: 225px; top: 134px; text-align: right; }
  .card-person .person-name { color: var(--brand-blue); font-weight: 700; font-size: 17px; }
  .card-person .person-title { font-size: 12px; margin-top: 1px; }
  .card-divider { position: absolute; left: 212px; top: 131px; width: 1px; height: 45px; background: var(--text-gray); }
  .contact-list { position: absolute; left: 226px; top: 130px; list-style: none; font-size: 12px; }
  .contact-list li { display: flex; align-items: center; gap: 5px; height: 15.5px; }
  .contact-list svg { width: 11px; height: 11px; fill: var(--brand-blue); }
  .card-address { position: absolute; left: 0; right: 0; top: 205px; text-align: center; font-size: 12px; }

  /* Business card back */
  .card-back { left: 618px; top: 58px; width: 425px; height: 242px; background: var(--ink); }
  .card-back .brand-name { top: 110px; font-size: 17px; }

  /* Letterhead */
  .letterhead { left: 39px; top: 337px; width: 540px; height: 765px; }
  .letterhead .brand-band { top: 32px; height: 23px; }
  .letterhead .band-blue { width: 264px; }
  .letterhead .brand-name { top: 37px; font-size: 12px; }
  .letterhead .brand-rule { top: 62px; height: 1px; }
  .letter-body { position: absolute; left: 48px; top: 234px; width: 445px; }
  .greeting { font-family: "Montserrat", Arial, sans-serif; font-weight: 600; font-size: 12px; color: var(--text-gray); margin-bottom: 20px; margin-left: 1px; }
  .letter-body p { font-size: 9px; line-height: 11.1px; margin-bottom: 9.5px; }
  .closing { font-family: "Montserrat", Arial, sans-serif; font-weight: 600; font-size: 7px; margin-top: 16px; }
  .signature-area { display: block; width: 90px; height: 28px; margin-top: 16px; background: linear-gradient(90deg, #d9d9dc, #ececef); border-radius: 3px; }
  .letter-footer { position: absolute; left: 0; right: 0; top: 704px; text-align: center; }
  .footer-name { font-size: 11px; }
  .footer-name strong { color: var(--brand-blue); }
  .footer-name span { color: var(--text-gray); font-size: 9px; }
  .footer-address { font-size: 9px; margin-top: 6px; }
  .footer-rule { width: 296px; height: 1px; background: var(--text-gray); margin: 3px auto 4px; }
  .footer-contacts { display: flex; justify-content: center; gap: 7px; font-size: 9px; }
  .footer-contacts span { display: flex; align-items: center; gap: 4px; }
  .footer-contacts svg { width: 7px; height: 7px; fill: var(--brand-blue); }

  /* Envelopes */
  .envelope { left: 618px; width: 543px; height: 236px; overflow: visible; }
  .envelope-flap { position: absolute; left: 0; top: 0; width: 543px; height: 66px; filter: drop-shadow(0 3px 3px rgba(0,0,0,.22)); }
  .envelope .brand-name { font-size: 11px; }
  .envelope-blue { top: 337px; }
  .envelope-blue .brand-name { top: 22px; }
  .envelope-white { top: 592px; }
  .envelope-white .brand-name { top: 22px; color: var(--ink); }
  .envelope-band { top: 866px; overflow: hidden; }
  .envelope-band .brand-band { top: 17px; height: 20px; }
  .envelope-band .band-blue { width: 270px; }
  .envelope-band .brand-name { top: 21px; }
  .envelope-band .brand-rule { top: 43px; height: 1px; }
  .envelope-address { position: absolute; left: 0; right: 0; top: 212px; text-align: center; font-size: 7.5px; color: #333; }
</style>
</head>
<body>

<svg width="0" height="0" style="position:absolute">
  <defs>
    <symbol id="icon-phone" viewBox="0 0 24 24"><path d="M6.6 10.8a15.1 15.1 0 0 0 6.6 6.6l2.2-2.2a1 1 0 0 1 1-.25 11.4 11.4 0 0 0 3.6.6 1 1 0 0 1 1 1V20a1 1 0 0 1-1 1A17 17 0 0 1 3 4a1 1 0 0 1 1-1h3.5a1 1 0 0 1 1 1c0 1.25.2 2.45.6 3.6a1 1 0 0 1-.25 1z"/></symbol>
    <symbol id="icon-mail" viewBox="0 0 24 24"><path d="M2 5h20v14H2z M2 5l10 8 10-8" fill="none" stroke="currentColor"/><path d="M2 5h20v14H2zm2 2v.4l8 6.3 8-6.3V7z"/></symbol>
    <symbol id="icon-globe" viewBox="0 0 24 24"><path d="M12 2a10 10 0 1 0 0 20 10 10 0 0 0 0-20zm-1 17.9A8 8 0 0 1 4.2 10L9 14.8V16a2 2 0 0 0 2 2zm6.9-2.5A2 2 0 0 0 16 16h-1v-3a1 1 0 0 0-1-1H8v-2h2a1 1 0 0 0 1-1V7h2a2 2 0 0 0 2-2v-.4a8 8 0 0 1 2.9 12.8z"/></symbol>
  </defs>
</svg>

<section class="sheet card-front" aria-label="Business card, front">
  <div class="brand-band"><div class="band-blue"></div><div class="band-black"></div></div>
  <div class="brand-name">Fernhallow Outdoor Advertising</div>
  <div class="brand-rule"></div>
  <div class="card-person">
    <div class="person-name">Dale Fernhallow</div>
    <div class="person-title">President</div>
  </div>
  <div class="card-divider"></div>
  <ul class="contact-list">
    <li><svg><use href="#icon-phone"/></svg>555-862-1907</li>
    <li><svg><use href="#icon-mail"/></svg>dale@fernhallowsigns.example</li>
    <li><svg><use href="#icon-globe"/></svg>fernhallowsigns.example</li>
  </ul>
  <div class="card-address">4873 Quarry Rd. 915 N. PO BOX 528617, Austin, TX 78519</div>
</section>

<section class="sheet card-back" aria-label="Business card, back">
  <div class="brand-name">Fernhallow Outdoor Advertising</div>
</section>

<section class="sheet letterhead" aria-label="Letterhead">
  <div class="brand-band"><div class="band-blue"></div><div class="band-black"></div></div>
  <div class="brand-name">Fernhallow Outdoor Advertising</div>
  <div class="brand-rule"></div>
  <div class="letter-body">
    <div class="greeting">Dear Mr. Smith,</div>
    <p>Lorem ipsum dolor sit amet, consectetuer adipiscing elit, sed diam nonmmy nibh euismod tincidunt ut laor eet dolore magna aliquam erat volutpat. Ut wisi enim ad minim veniam, quis nostrud exerci tationmcorper suscipit lobortis nisl ut aliquip ex ea commodo consequat. Duis autem vel eum iriure dolor in hendrerit in vulputate velit esse molestie consequat, vel illum dolore eu feugiat</p>
    <p>Rorem ipsum dolor sit amet, consectetuer adipiscing elit, sed diam nonmmy nibh euismod tincidunt ut laor eet dolore magna aliquam erat volutpat. Ut wisi enim ad minim veniam, quis nostrud exerci tationmcorper suscipit lobortis nisl ut aliquip ex ea commodo consequat. Duis autem vel eum iriure dolor in hendrerit in vulputate velit esse molest</p>
    <p>Dorem ipsum dolor sit amet, consectetuer adipiscing elit, sed diam nonmmy nibh euismod tincidunt ut laor eet dolore magna aliquam erat volutpat. Ut wisi enim ad minim veniam, quis nostrud exerci tationmcorper suscipit lobortis nisl ut aliquip ex ea commodo consequat. Duis autem vel eum iriure dolor in hendrerit in suscipit lobortis nisl ut aliquip ex ea commodo consequat. Duis autem vel eum iriure dolor in hendrerit in vulputate velit esse molestie consequat, vel illum</p>
    <p>Sorem ipsum dolor sit amet, consectetuer adipiscing elit, sed diam nonmmy nibh euismod tincidunt ut laor eet dolore magna aliquam erat volutpat. Ut wisi enim ad minim veniam, quis nostrud exerci tationmcorper suscipit lobortis nisl ut aliquip ex ea commodo consequat. Duis autem vel eum iriure dolor in</p>
    <div class="closing">Sincerely,</div>
    <span class="signature-area" role="img" aria-label="Handwritten signature"></span>
  </div>
  <footer class="letter-footer">
    <div class="footer-name"><strong>Dale Fernhallow | </strong><span>President</span></div>
    <div class="footer-address">4873 Quarry Rd. 915 N. PO BOX 528617, Austin, TX 78519</div>
    <div class="footer-rule"></div>
    <div class="footer-contacts">
      <span><svg><use href="#icon-phone"/></svg>555-862-1907</span>
      <span><svg><use href="#icon-mail"/></svg>dale@fernhallowsigns.example</span>
      <span><svg><use href="#icon-globe"/></svg>fernhallowsigns.example</span>
    </div>
  </footer>
</section>

<section class="sheet envelope envelope-blue" aria-label="Envelope, back with blue flap">
  <svg class="envelope-flap" viewBox="0 0 543 66" aria-hidden="true">
    <path d="M0 0H543L530 50Q525 64 506 64H38Q19 64 13 50Z" fill="var(--brand-blue)"/>
  </svg>
  <div class="brand-name">Fernhallow Outdoor Advertising</div>
</section>

<section class="sheet envelope envelope-white" aria-label="Envelope, back with white flap">
  <svg class="envelope-flap" viewBox="0 0 543 66" aria-hidden="true">
    <path d="M0 0H543L530 50Q525 64 506 64H38Q19 64 13 50Z" fill="#ffffff"/>
  </svg>
  <div class="brand-name">Fernhallow Outdoor Advertising</div>
</section>

<section class="sheet envelope envelope-band" aria-label="Envelope, front">
  <div class="brand-band"><div class="band-blue"></div><div class="band-black"></div></div>
  <div class="brand-name">Fernhallow Outdoor Advertising</div>
  <div class="brand-rule"></div>
  <div class="envelope-address">4873 Quarry Rd. 915 N. PO BOX 528617, Austin, TX 78519</div>
</section>

</body>
</html>
```